Glen Holbrook Announces his new career move! 8x5 card please.

Associate Broker GLEN HOLBROOK is proud to announce his new affiliation with m.vorlund bayshore estates, ltd.

His goal remains to meet all your real estate needs. Prepare to renew your seasonal rental for 2016...with the full support of his new office, Glen can handle your renewal seamlessly.

Prepared to purchase? With access to every property on the market...Glen can show you how easy it making your summer dreams come true can be.

Thinking about selling? m.vorlund bayshore estates, ltd. now offers the benefits of the Multiple Listing Service (MLS) to all sellers. In cooperation with MLS Sellers receive the maximum worldwide exposure, Purchasers receive a larger volume of properties to view and in cooperation with other Realtors, the transaction is handled professionally!!!!

I will send logo and photo of Glen Holbrook separately. Thank you. P-
Updates

Target Market(s)

Tenants, Sellers & Buyers

Industry/Entity Type

Broker

Font styles to use
Sans Serif

Requirements
Must have
• I attached logo and photo of Glen. Added a better photo of Glen.
Nice to have
• A photo of a property we have listed. I added a couple to choose from.
Should not have
• No Red color

```html
<!DOCTYPE html>
<html lang="en">
<head>
<meta charset="utf-8">
<title>Glen Holbrook – Announcement Postcard</title>
<link href="https://fonts.googleapis.com/css2?family=Open+Sans:wght@300;400;600;700&display=swap" rel="stylesheet">
<style>
  :root {
    --green: #0f7f4a;
    --green-dark: #0b6b3d;
    --charcoal: #3b3b3d;
    --grey-mid: #b9babc;
    --grey-light: #e6e7e8;
    --paper: #ffffff;
    --ink: #333333;
    --backdrop: #eeeeec;
    --stamp: #a7a9ac;
  }
  * { margin: 0; padding: 0; box-sizing: border-box; }
  html, body { width: 860px; height: 1200px; overflow: hidden; }
  body {
    background: var(--backdrop);
    font-family: "Open Sans", Arial, sans-serif;
    color: var(--ink);
    position: relative;
  }
  .card { position: absolute; left: 83px; width: 712px; height: 508px; overflow: hidden; }
  .card-front { top: 92px; background: var(--paper); }
  .card-back { top: 628px; height: 509px; background: var(--grey-light); }

  /* front */
  .header-swoosh { position: absolute; left: 0; top: 0; }
  .brand-name {
    position: absolute; left: 42px; top: 32px;
    font-size: 31px; font-weight: 700; color: var(--paper);
    letter-spacing: -0.5px; display: flex; align-items: center; gap: 12px;
    white-space: nowrap;
  }
  .brand-square { width: 15px; height: 15px; background: var(--paper); display: inline-block; flex: none; }
  .announcement {
    position: absolute; left: 38px; top: 196px; width: 580px;
    font-size: 18px; font-weight: 700; color: var(--green); line-height: 1.4;
  }
  .rental-banner { position: absolute; left: 0; top: 267px; }
  .rental-text {
    position: absolute; left: 36px; top: 274px; width: 510px;
    font-size: 11px; font-weight: 700; color: var(--paper); line-height: 1.55;
  }
  .column { position: absolute; top: 340px; }
  .column h2 { font-size: 16.5px; font-weight: 700; color: var(--green); margin-bottom: 12px; }
  .column p { font-size: 11.2px; line-height: 1.5; color: var(--ink); text-align: justify; }
  .col-purchase { left: 38px; width: 188px; }
  .col-selling { left: 262px; width: 418px; }
  .web-tab { position: absolute; right: 35px; bottom: 0; }
  .web-address {
    position: absolute; left: 388px; top: 475px; width: 280px; text-align: center;
    font-size: 19px; font-weight: 600; color: var(--paper);
  }

  /* back */
  .top-strip { position: absolute; left: 0; top: 0; width: 712px; height: 12px; background: #111; }
  .promo-panel { position: absolute; left: 0; top: 12px; width: 425px; height: 397px; background: var(--green); }
  .homes-title {
    position: absolute; left: 0; top: 12px; width: 425px; height: 55px;
    background: var(--green-dark);
    font-size: 21px; font-weight: 300; color: var(--paper);
    padding: 13px 0 0 24px; letter-spacing: -0.2px; white-space: nowrap;
  }
  .homes-title strong { font-weight: 700; }
  .property-photo { position: absolute; top: 75px; width: 133px; height: 99px; }
  .photo-kitchen { left: 8px; background: linear-gradient(135deg, #6b4a2c, #a08260 55%, #d8d4cc); }
  .photo-pool { left: 145px; background: linear-gradient(180deg, #6f9bd2 0%, #e9eef2 45%, #3aa6d6 75%, #2478b8); }
  .photo-bedroom { left: 280px; background: linear-gradient(135deg, #8db46a, #e7e4dc 45%, #f1efea 70%, #b6a692); }
  .back-brand {
    position: absolute; left: 18px; top: 193px; width: 400px;
    font-size: 22px; font-weight: 700; color: var(--paper);
    letter-spacing: -0.4px; display: flex; align-items: center; gap: 9px;
    white-space: nowrap;
  }
  .back-brand .brand-square { width: 12px; height: 12px; }
  .broker-portrait {
    position: absolute; left: 273px; top: 237px; width: 122px; height: 145px;
    border-radius: 6px; border: 2px solid #dfe8e3;
    background: linear-gradient(180deg, #b7cbd8 0%, #c9b8a4 50%, #3b2f2c 100%);
  }
  .broker-info { position: absolute; left: 0; top: 280px; width: 252px; text-align: right; color: var(--paper); }
  .broker-name { font-size: 21px; font-weight: 700; line-height: 1.15; }
  .broker-title { font-size: 18px; font-weight: 300; margin-bottom: 14px; }
  .broker-office { font-size: 11px; font-weight: 700; line-height: 1.45; }
  .broker-address { font-size: 11px; line-height: 1.45; }
  .contact-bar {
    position: absolute; left: 0; top: 409px; width: 425px; height: 26px;
    background: var(--charcoal); color: var(--paper);
    font-size: 13.5px; font-weight: 600; padding: 4px 0 0 30px; word-spacing: 2px;
    white-space: nowrap;
  }
  .contact-bar span + span { margin-left: 26px; }
  .stamp-box { position: absolute; left: 584px; top: 32px; width: 104px; height: 108px; background: var(--stamp); border-radius: 8px; }
  .address-line { position: absolute; left: 450px; width: 232px; height: 1px; background: #8a8c8e; }
  .postal-area { position: absolute; left: 122px; top: 466px; font-size: 9px; font-weight: 700; color: var(--ink); }
</style>
</head>
<body>

<section class="card card-front">
  <svg class="header-swoosh" width="712" height="180" viewBox="0 0 712 180" aria-hidden="true">
    <path d="M0 50 C200 120 480 150 712 40 L712 60 C480 175 220 165 0 140 Z" fill="var(--grey-mid)"/>
    <path d="M0 82 C200 135 470 140 712 30 L712 45 C480 160 220 150 0 118 Z" fill="var(--charcoal)"/>
    <path d="M0 0 H712 V28 C480 132 220 128 0 85 Z" fill="var(--green)"/>
  </svg>
  <div class="brand-name"><span class="brand-square"></span>m.vorlund bayshore estates, ltd.</div>

  <h1 class="announcement">Associate Broker GLEN HOLBROOK is proud to announce his new affiliation with m.vorlund bayshore estates, ltd.</h1>

  <svg class="rental-banner" width="580" height="50" viewBox="0 0 580 50" aria-hidden="true">
    <path d="M0 0 H555 L575 25 L555 50 H0 Z" fill="var(--green)"/>
  </svg>
  <p class="rental-text">His goal remains to meet all your real estate needs. Prepare to renew your seasonal rental for 2016...with the full support of his new office, Glen can handle your renewal seamlessly.</p>

  <div class="column col-purchase">
    <h2>Prepared to purchase?</h2>
    <p>With access to every property on the market...Glen can show you how easy it making your summer dreams come true can be.</p>
  </div>
  <div class="column col-selling">
    <h2>Thinking about selling?</h2>
    <p>m.vorlund bayshore estates, ltd. now offers the benefits of the Multiple Listing Service (MLS) to all sellers. In cooperation with MLS Sellers receive the maximum worldwide exposure, Purchasers receive a larger volume of properties to view and in cooperation with other Realtors, the transaction is handled professionally!!!!</p>
  </div>

  <svg class="web-tab" width="330" height="42" viewBox="0 0 330 42" aria-hidden="true">
    <path d="M0 42 C10 20 16 2 40 2 H290 C314 2 320 20 330 42 Z" fill="var(--green)"/>
  </svg>
  <div class="web-address">www.bayshoreestates.com</div>
</section>

<section class="card card-back">
  <div class="top-strip"></div>
  <div class="promo-panel"></div>
  <div class="homes-title">the fabulous homes of <strong>bayshore harbor</strong></div>
  <div class="property-photo photo-kitchen" role="img" aria-label="Photo of a listed home's wooden kitchen"></div>
  <div class="property-photo photo-pool" role="img" aria-label="Photo of a white house with a backyard pool"></div>
  <div class="property-photo photo-bedroom" role="img" aria-label="Photo of a bright bedroom with garden view"></div>

  <div class="back-brand"><span class="brand-square"></span>m.vorlund bayshore estates, ltd.</div>

  <div class="broker-info">
    <div class="broker-name">GLEN HOLBROOK</div>
    <div class="broker-title">Associate Broker</div>
    <div class="broker-office">m. vorlund bayshore estates, ltd.</div>
    <div class="broker-address">on the harbor, P.O. Box 4821, Bayshore<br>Harbor, NY 11790</div>
  </div>
  <div class="broker-portrait" role="img" aria-label="Portrait photo of Glen Holbrook"></div>

  <div class="contact-bar"><span>fax: 555-314-2086</span><span>e-mail: info@bayshoreestates.com</span></div>

  <div class="stamp-box"></div>
  <div class="address-line" style="top:329px"></div>
  <div class="address-line" style="top:365px"></div>
  <div class="address-line" style="top:402px"></div>
  <div class="address-line" style="top:438px"></div>

  <div class="postal-area">barcode &amp; postal marketing area</div>
</section>

</body>
</html>
```